(Harbour Roastworks) sourcing coffee related material and services

we are a start up that provide all coffee related items for coffee shops and coffee fanatics. However, we mostly offer coffee machines customization that includes paint replacement and wood modification. we also focus on providing training for barista and coffee lovers.

we are looking for the following:

1-Design a logo that will be used for social media application and official paper work requirements

2- Design a business card (square shaped 2"*2") adopting the same logo and identity. please allow for adding mobile number, snapchat, and instgram accounts in the card.

3- Design a very basic monogram stamp by adding the three character (R4T) the number (2) shall be small in size just like how the numbers written in chemical formal.

Please take a quick look to instagram page to have a idea about the our start up

https://www.pixgram.example/harbour_roastworks/

Target Market(s)

coffeeshop owners and coffee fanatics

Industry/Entity Type

Coffee Shop

Contact Information for Business Card

R4T
Harbour Roastworks
editable text to add links to socail media

Logo Text

R4T

Font styles to use
Other font styles liked:
• flat design fonts

Colors

Designer to choose colors to be used in the design.

Requirements
Must have
• espresso portafilter, simple and minimal industrial look, wood,
Nice to have
• wood-making, portafilter, coffee beans, coffee tree,

```html
<!DOCTYPE html>
<html lang="en">
<head>
<meta charset="UTF-8">
<title>Harbour Roastworks — Business Card</title>
<link rel="stylesheet" href="https://fonts.googleapis.com/css2?family=Exo+2:wght@600&family=Montserrat:wght@500&family=Arimo:wght@400&display=swap">
<style>
  :root {
    --page: #ffffff;
    --beans-light-top: #cfc3a6;
    --beans-light-bottom: #bfae8c;
    --beans-dark-top: #6b3a24;
    --beans-dark-mid: #8a4c30;
    --beans-dark-bottom: #4e2a1a;
    --panel: #d3c8ab;
    --ink: #231c18;
    --rule: #8a5a2e;
  }
  * { margin: 0; padding: 0; box-sizing: border-box; }
  html, body {
    width: 1200px;
    height: 1200px;
    overflow: hidden;
    background: var(--page);
  }
  .canvas {
    position: relative;
    width: 1200px;
    height: 1200px;
  }
  .card {
    position: absolute;
    left: 209px;
    top: 209px;
    width: 772px;
    height: 772px;
    overflow: hidden;
  }
  .beans-faded {
    position: absolute;
    left: 0; top: 0;
    width: 100%;
    height: 385px;
    background: linear-gradient(180deg, var(--beans-light-top), var(--beans-light-bottom));
  }
  .beans-roasted {
    position: absolute;
    left: 0; top: 385px;
    width: 100%;
    height: 387px;
    background: radial-gradient(ellipse at 40% 50%, var(--beans-dark-mid), var(--beans-dark-top) 55%, var(--beans-dark-bottom));
  }
  .info-panel {
    position: absolute;
    left: 120px;
    top: 120px;
    width: 532px;
    height: 532px;
    background: var(--panel);
    text-align: center;
    color: var(--ink);
  }
  .brand-code {
    position: absolute;
    left: 0; right: 0;
    top: 118px;
    font-family: "Exo 2", sans-serif;
    font-weight: 600;
    font-size: 22px;
    letter-spacing: 4px;
    color: var(--ink);
  }
  .brand-name {
    position: absolute;
    left: 0; right: 0;
    top: 160px;
    font-family: "Exo 2", sans-serif;
    font-weight: 600;
    font-size: 33px;
    letter-spacing: 2px;
    text-transform: uppercase;
    color: var(--ink);
  }
  .tagline {
    position: absolute;
    left: 0; right: 0;
    top: 280px;
    font-family: "Montserrat", sans-serif;
    font-weight: 500;
    font-size: 14px;
    letter-spacing: 1.2px;
  }
  .contact {
    position: absolute;
    left: 0; right: 0;
    top: 420px;
    font-family: "Arimo", sans-serif;
    font-size: 18.5px;
    line-height: 28px;
  }
  .contact-rule {
    width: 420px;
    height: 1px;
    margin: 6px auto 4px;
    background: var(--rule);
  }
</style>
</head>
<body>
  <div class="canvas">
    <section class="card">
      <div class="beans-faded" role="img" aria-label="Faded photograph of roasted coffee beans"></div>
      <div class="beans-roasted" role="img" aria-label="Photograph of dark roasted coffee beans"></div>

      <div class="info-panel">
        <div class="brand-code">R4T</div>
        <div class="brand-name">Harbour Roastworks</div>
        <p class="tagline">Sourcing Coffee Related Material &amp; Services</p>
        <div class="contact">
          <p>Add snapchat account here</p>
          <p>Add instagram account here</p>
          <div class="contact-rule"></div>
          <p>Add mobile number here</p>
        </div>
      </div>
    </section>
  </div>
</body>
</html>
```